Letterhead design for a vibrant telco business using our wonderful logo

We need an elegant and captivating letterhead design that takes advantage of our bright and colourful logo and reflects our brand name "Copper Wharf".
We are positioned as a fresh, vibrant and innovative VoIP carrier servicing the business market in Australia
We have a great website design that's flowed through to existing business card design. I can supply the CMYK colour details and font details as required.
There will be several other design jobs following this one for our brand.
Target Market(s)
Standard business correspondence. Mostly will be PDF'ing documents, some physical colour printing.
Industry/Entity Type
Telecommunications

```html
<!DOCTYPE html>
<html lang="en">
<head>
<meta charset="utf-8">
<title>Copper Wharf Letterhead</title>
<link href="https://fonts.googleapis.com/css2?family=Montserrat:wght@400;600&display=swap" rel="stylesheet">
<style>
  :root {
    --ink: #3a3a3c;
    --text: #333333;
    --rule-dark: #2b2b2b;
    --rule-light: #b9b9b9;
    --paper: #ffffff;
    --tint-green: #e7f4e6;
    --tint-blue: #e4ecf8;
    --tint-violet: #ece6f5;
    --tint-pink: #f8e4ec;
    --tint-peach: #fdeee2;
    --tint-cream: #fef6e8;
  }
  * { margin: 0; padding: 0; box-sizing: border-box; }
  html, body { width: 849px; height: 1200px; overflow: hidden; background: var(--paper); }
  .letterhead {
    position: relative;
    width: 849px;
    height: 1200px;
    background: var(--paper);
    font-family: "Montserrat", sans-serif;
    color: var(--text);
  }
  .brand {
    position: absolute;
    top: 40px;
    left: 0;
    width: 100%;
    display: flex;
    justify-content: center;
    align-items: center;
    gap: 18px;
  }
  .brand-square {
    width: 100px;
    height: 100px;
    background: var(--tint-pink);
  }
  .brand-name {
    font-weight: 600;
    font-size: 50px;
    line-height: 50px;
    letter-spacing: 1px;
    color: var(--ink);
    text-transform: uppercase;
  }
  .header-rule {
    position: absolute;
    top: 162px;
    left: 0;
    width: 100%;
    height: 3px;
    background: var(--rule-dark);
  }
  .header-rule::after {
    content: "";
    position: absolute;
    top: 7px;
    left: 0;
    width: 100%;
    height: 1px;
    background: var(--rule-light);
  }
  .decor-band {
    position: absolute;
    top: 226px;
    left: 425px;
    width: 424px;
    height: 780px;
    background:
      linear-gradient(90deg, var(--paper) 0%, rgba(255,255,255,0) 18%),
      linear-gradient(180deg,
        var(--tint-green) 0%,
        var(--tint-blue) 22%,
        var(--tint-violet) 42%,
        var(--tint-pink) 60%,
        var(--tint-peach) 80%,
        var(--tint-cream) 100%);
  }
  .footer-rule {
    position: absolute;
    top: 1076px;
    left: 0;
    width: 100%;
    height: 3px;
    background: var(--rule-dark);
  }
  .contact {
    position: absolute;
    top: 1094px;
    left: 0;
    width: 100%;
    text-align: center;
    font-size: 19px;
    line-height: 23px;
    color: var(--text);
  }
  .contact b { font-weight: 600; }
  .contact .sep { margin: 0 6px; font-weight: 600; }
</style>
</head>
<body>
  <main class="letterhead">
    <header class="brand">
      <div class="brand-square"></div>
      <div class="brand-name">Copper<br>Wharf</div>
    </header>
    <div class="header-rule"></div>

    <div class="decor-band" role="img" aria-label="Soft sweeping bands of pale brand colours from green through blue, violet, pink and peach"></div>

    <div class="footer-rule"></div>
    <footer class="contact">
      <div><b>M</b> 0412 555 018<span class="sep">|</span><b>P</b> 1300 555 210<span class="sep">|</span><b>F</b> 1300 555 211</div>
      <div><b>E</b> alexr@copperwharf.com.au</div>
      <div>www.copperwharf.com.au</div>
    </footer>
  </main>
</body>
</html>
```